Optometric Practice needs Initial Photoshop Mockup

We need a graphic design for the homepage of a website for an optometric practice that specializes in vision therapy.

Here's the link to the project folder on Stashly. I've included photos, example sites, content and instructions.

https://www.stashly-files.example/sh/k2wq8rn5tz1xv3m/BQX_LmRtYpeKa7NzHdVcWUbQo

Please feel free to submit any questions about the design. I'll be happy to help guide you in any areas you're uncertain of.

Okay - I've updated the project to payment confirmed. Let's see some designs :) Thanks, Reg

```html
<!DOCTYPE html>
<html lang="en">
<head>
<meta charset="utf-8">
<title>Clearpath Vision Centers – Home</title>
<link href="https://fonts.googleapis.com/css2?family=PT+Sans:wght@400;700&family=Open+Sans:wght@400;600&display=swap" rel="stylesheet">
<style>
:root{
  --cream:#f3ecd3;
  --cream-light:#f8f3e2;
  --cream-dark:#e9dfc0;
  --red:#a50d10;
  --red-dark:#7e0709;
  --navy:#2d2f86;
  --ink:#3a3a3a;
  --grey:#8b8b86;
  --line:#d9cfb0;
}
*{box-sizing:border-box;margin:0;padding:0}
html,body{width:695px;height:1200px;overflow:hidden}
body{background:var(--cream);font-family:"Open Sans",sans-serif;color:var(--ink);position:relative}
.abs{position:absolute}
.top-rule{left:0;top:0;width:695px;height:4px;background:var(--red)}
.header-contact{left:68px;top:11px;font-size:6.4px;color:var(--grey);line-height:8px;display:flex;gap:8px}
.header-contact span{display:flex;gap:4px}
.header-contact svg{flex:none}
.brand{left:298px;top:16px;width:100px;text-align:center;font-family:"PT Sans",sans-serif;font-weight:700;font-size:17px;color:var(--red);letter-spacing:2px}
.appt{left:505px;top:4px;width:121px;height:29px;background:var(--red);border-radius:0 0 4px 4px;color:#fff;font-family:"PT Sans",sans-serif;display:flex;align-items:center;gap:6px;padding-left:8px}
.appt .ico{width:19px;height:19px;border-radius:50%;background:#fff;display:flex;align-items:center;justify-content:center}
.appt small{display:block;font-size:8px;font-weight:700;line-height:9px}
.appt b{display:block;font-size:11.5px;line-height:12px}
.nav{left:76px;top:80px;display:flex;gap:0;font-size:7.4px;color:#555;width:545px;justify-content:space-between}
.nav .current{color:var(--red)}
.hero{left:0;top:112px;width:695px;height:214px}
.hero-photo{position:absolute;inset:0;background:linear-gradient(90deg,#d9d6cf 0%,#3e5a4a 30%,#2f4c40 70%,#d7d3cb 100%)}
.caption{left:226px;top:214px;width:243px;height:69px;background:rgba(222,226,190,.82);border:1px solid rgba(255,255,255,.6);text-align:center;padding-top:13px}
.caption h2{font-family:"PT Sans",sans-serif;font-size:14.5px;color:var(--navy);font-weight:700}
.caption p{font-size:7px;color:#4a4a8a;line-height:9px;margin-top:2px}
.dots{left:306px;top:318px;display:flex;gap:6px}
.dots i{width:7px;height:7px;border-radius:50%;border:1px solid #ccc;background:#fff}
.dots i.on{background:var(--red);border-color:var(--red)}
.promos{left:69px;top:364px;width:557px;height:45px;display:flex;gap:2px}
.promos a{flex:1;background:var(--red);color:#fff;font-family:"PT Sans",sans-serif;font-weight:700;font-size:8.6px;line-height:10.5px;display:flex;align-items:center;justify-content:center;text-align:center;padding:0 10px;text-decoration:none;border:1px solid var(--red-dark)}
.video-band{left:0;top:435px;width:695px;height:250px}
.feat-title{left:69px;top:478px;display:flex;align-items:center;gap:6px;font-family:"PT Sans",sans-serif;font-weight:700;font-size:15px;color:var(--navy)}
.feat-text{left:69px;top:516px;width:158px;font-size:6px;line-height:10px;color:#a09c90}
.feat-text p+p{margin-top:10px}
.player{left:258px;top:472px;width:368px;height:182px;background:#222}
.player .bar{position:absolute;left:0;top:0;width:100%;height:18px;background:#1c3f74;color:#fff;font-size:5px;padding:6px 8px}
.player .frame{position:absolute;left:0;top:18px;width:100%;height:127px;background:linear-gradient(90deg,#3a2a1f 0%,#7a5a3a 35%,#4a3a5a 60%,#2d4a8a 100%)}
.player .track{position:absolute;left:0;top:145px;width:100%;height:37px;background:linear-gradient(#eee,#cfcfcf)}
.player .brand-mark{position:absolute;right:34px;bottom:5px;color:#3fb5e8;font-family:"PT Sans",sans-serif;font-size:11px;font-weight:700}
.divider-mark{left:341px;top:684px;width:12px;height:12px;border-radius:50%;background:var(--navy)}
.h1{font-family:"PT Sans",sans-serif;font-size:19px;font-weight:400}
.welcome{left:69px;top:724px;color:var(--navy)}
.doc-photo{left:69px;top:757px;width:136px;height:121px;background:linear-gradient(135deg,#e7dccd,#c9a08c 55%,#e9e3d8);border:2px solid #fff;box-shadow:0 0 0 1px var(--line)}
.intro{left:215px;top:757px;width:243px}
.intro h3{font-family:"PT Sans",sans-serif;font-weight:400;font-size:12.5px;line-height:12px;color:var(--red)}
.intro p{font-size:6.1px;line-height:8.3px;color:var(--grey);margin-top:6px}
.services{left:69px;top:893px;width:360px;list-style:none}
.services li{position:relative;padding-left:13px;font-size:6.1px;line-height:8.3px;color:var(--grey);margin-bottom:7.5px}
.services li::before{content:"";position:absolute;left:0;top:1px;width:5px;height:5px;border:1px solid #666;border-radius:50%}
.special{left:477px;top:724px;color:var(--red)}
.solutions{left:477px;top:757px;width:150px}
.solutions div{margin-bottom:14px}
.solutions h4{font-weight:400;font-size:7.8px;color:#333}
.solutions p{font-size:5.8px;line-height:10px;color:#aaa}
.solutions a{font-size:6.2px;color:#333;text-decoration:none}
.social-box{left:475px;top:925px;width:151px;height:138px;background:#fff;border:1px solid #c9c9c9;font-family:Arial,sans-serif}
.social-box .hd{font-size:5.4px;padding:3px;border-bottom:1px solid #ddd;background:#f4f4f4}
.social-box .pg{display:flex;gap:4px;padding:5px}
.social-box .pg .av{width:25px;height:25px;background:#d9c8bb}
.social-box .pg b{font-size:6.4px;color:#3b5998;line-height:8px;display:block}
.social-box .pg em{display:inline-block;font-style:normal;background:#4a66a0;color:#fff;font-size:5px;padding:1px 3px;margin-top:2px}
.social-box .cnt{font-size:5px;color:#777;padding:3px 5px;border-top:1px solid #eee;line-height:7px}
.social-box .faces{display:grid;grid-template-columns:repeat(5,25px);gap:2px;padding:3px 5px}
.social-box .faces i{height:25px;background:#b9b4ad}
.footer{left:0;top:1100px;width:695px;height:100px;background:var(--cream-dark);border-top:1px solid var(--line)}
.f-brand{left:69px;top:1121px;font-family:"PT Sans",sans-serif;font-weight:700;font-size:14px;color:var(--red);letter-spacing:2px}
.f-copy{left:69px;top:1152px;font-size:5.8px;color:#555}
.f-social{left:69px;top:1166px;display:flex;gap:4px}
.f-social i{width:14px;height:14px;background:#5a7fbf;display:block}
.f-social i:nth-child(2),.f-social i:nth-child(3){background:#c8332f}
.f-addr{font-size:6.3px;line-height:8.2px;color:#555}
.f-links{left:489px;top:1122px;font-family:"PT Sans",sans-serif}
.f-links h5{font-weight:400;font-size:8.6px;color:var(--red)}
.f-links .cols{display:flex;gap:17px;margin-top:6px;font-size:6.2px;line-height:8.5px;color:#555}
.f-links .cols span:first-child{color:var(--red)}
</style>
</head>
<body>
<div class="abs top-rule"></div>

<div class="abs header-contact">
  <span><svg width="8" height="9" viewBox="0 0 8 9"><path d="M4 8.5C1.5 5.5 1 4.5 1 3.3a3 3 0 0 1 6 0c0 1.2-.5 2.2-3 5.2z" fill="none" stroke="#a50d10" stroke-width="1"/><circle cx="4" cy="3.3" r="1" fill="#a50d10"/></svg><span>Clearpath Vision Centers,<br>Inc. Dr. Daniel Averin</span></span>
  <span><svg width="8" height="8" viewBox="0 0 8 8"><path d="M1.5 1 3 .8 3.8 2.6 3 3.4a5 5 0 0 0 1.6 1.6l.8-.8 1.8.8-.2 1.5C4 6.8 1.2 4 1.5 1z" fill="none" stroke="#a50d10" stroke-width=".9"/></svg>410-555-0142</span>
</div>
<div class="abs brand">CVC</div>
<a class="abs appt"><span class="ico"><svg width="11" height="11" viewBox="0 0 11 11"><rect x="1" y="2" width="9" height="8" fill="none" stroke="#a50d10"/><path d="M1 4.5h9M3 1v2M8 1v2" stroke="#a50d10"/></svg></span><span><small>Request an</small><b>Appointment</b></span></a>

<nav class="abs nav">
  <span class="current">Home</span><span>Meet Us</span><span>New Patients</span><span>Vision &amp; Learning</span><span>Vision Therapy</span><span>Binocular Vision Disorders</span><span>Head Injuries</span><span>Professionals</span><span>Contact Us</span>
</nav>

<section class="abs hero">
  <div class="hero-photo" role="img" aria-label="Photo of a girl wearing vision therapy glasses pointing at a chalkboard beside rotating therapy charts"></div>
  <svg class="abs" style="left:0;top:0" width="695" height="214" viewBox="0 0 695 214">
    <path d="M0 0H695V10Q348 -14 0 10Z" fill="#f3ecd3"/>
    <path d="M0 10Q348 -14 695 10" fill="none" stroke="#a50d10" stroke-width="3"/>
    <path d="M0 214H695V206Q348 176 0 206Z" fill="#f3ecd3"/>
    <path d="M0 206Q348 176 695 206" fill="none" stroke="#a50d10" stroke-width="3"/>
  </svg>
</section>
<div class="abs caption">
  <h2>Improving Vision, Changing Lives</h2>
  <p>Happy kids, or a collage of their photos of kids getting<br>Vision Therapy.</p>
</div>
<div class="abs dots"><i class="on"></i><i></i><i></i><i></i></div>

<div class="abs promos">
  <a>Bright Child Struggling with Reading? It could be a vision problem.</a>
  <a>Improve Your Sports Performance</a>
  <a>Is it really ADD/ADHD?</a>
  <a>There is more to healthy vision that 20/20 eyesight</a>
</div>

<svg class="abs video-band" width="695" height="250" viewBox="0 0 695 250">
  <path d="M0 10Q348 -12 695 10V240Q348 218 0 240Z" fill="#f8f3e2"/>
</svg>
<div class="abs feat-title">
  <svg width="25" height="21" viewBox="0 0 25 21"><circle cx="5" cy="4" r="4" fill="#2d2f86"/><circle cx="13" cy="4" r="4" fill="#2d2f86"/><rect x="1" y="9" width="16" height="11" rx="1" fill="#2d2f86"/><path d="M18 12l6-3v11l-6-3z" fill="#2d2f86"/><rect x="4" y="12" width="10" height="5" fill="#f8f3e2"/></svg>
  Featured Video
</div>
<div class="abs feat-text">
  <p>Sed quis arcu suscipit, blandit odio id, placerat lectus. Fusce sed ultrices lectus. In nec fringilla velit. Suspendisse vel ante velit. Aliquam sagittis nulla vel tortor eleifend adipiscing. Nullam in odio consectetur, ornare sem et, auctor libero.</p>
  <p>Nam tortor nulla, vehicula ut euismod facilisis, adipiscing sit amet nibh. Donec feugiat fermentum mi vitae dignissim. Nam vulputate placerat dapibus.</p>
</div>
<div class="abs player">
  <div class="bar">Done</div>
  <div class="frame" role="img" aria-label="Video still of a television news presenter in a studio"></div>
  <div class="track">
    <svg width="368" height="37" viewBox="0 0 368 37">
      <rect x="60" y="6" width="344" height="3" rx="1.5" fill="#999"/>
      <circle cx="62" cy="7.5" r="5" fill="#eee" stroke="#aaa"/>
      <path d="M130 37Q150 14 175 14H368V37Z" fill="#1d1d1d"/>
      <circle cx="20" cy="24" r="9" fill="#ddd" stroke="#aaa"/>
      <path d="M17 20v8l7-4z" fill="#555"/>
      <rect x="51" y="21" width="6" height="6" fill="#666"/>
      <path d="M336 20l5 0 0 5M336 30l-5 0 0-5" stroke="#fff" fill="none"/>
      <circle cx="355" cy="25" r="4" fill="none" stroke="#fff" stroke-width="2"/>
    </svg>
    <span class="brand-mark">Clipwell</span>
  </div>
</div>
<div class="abs divider-mark"></div>

<h2 class="abs h1 welcome">Welcome to CVC</h2>
<div class="abs doc-photo" role="img" aria-label="Portrait photo of Dr. Daniel Averin"></div>
<div class="abs intro">
  <h3>There are many visual skills critical for reading and learning.</h3>
  <p>Often, a vision problem is misdiagnosed as an attention problem or a learning disability due to similarity of symptoms. Anyone who is struggling with reading, has poor reading comprehension, or just isn't performing to their full potential, should consider scheduling a developmental vision evaluation. To help determine if you or your child should be tested, Do the Checklist on our Vision Quiz page.<br>Dr. Daniel Averin is a developmental optometrist who specializes in the diagnosis and treatment of vision problems that interfere with reading and learning. He is a member of the National Optometric Society, the Guild of Developmental Optometrists, and a Fellow in the Academy of Clinical Optometry.</p>
</div>
<ul class="abs services">
  <li>Comprehensive Eye Examinations for All Ages, including Infants and Preschoolers</li>
  <li>Vision Therapy for All Ages</li>
  <li>Treatment for Learning-related Vision Problems</li>
  <li>Free Monthly Seminars. Visit our Friendbook page for information about our free monthly seminars on a variety of topics, including: The Hidden Disability - Undiagnosed Vision Problems</li>
  <li>Continuing Education seminars for Optometrists, Occupational Therapists and Physical Therapists. All CE offerings are free and board approved. For CE information and dates, see our success stories, blogs and videos on Binocular Vision Disorders</li>
  <li>Treatment for Binocular Vision Conditions, such as Amblyopia or Lazy Eye, Convergence Insufficiency (near vision disorder), Diplopia (double vision), Lack of Stereopsis (two-eyed depth perception), and Strabismus (cross-eyed, wandering eye, eye turns, etc.)</li>
  <li>Visual Rehabilitation for Patients with Special Needs, such as Developmental Delays or Traumatic Brain Injury (TBI), including Autism, Stroke, Whiplash, CP, MS, etc.</li>
  <li>Treatment for Stress-related Visual Problems, including Blurred Vision, Visual Stress from Reading and Computers, Eye Strain Headaches, and/or Vision-induced Stomachaches or Motion Sickness</li>
  <li>Sports Vision Correction and/or Improvement</li>
</ul>

<h2 class="abs h1 special">Special solutions</h2>
<div class="abs solutions">
  <div><h4>Nam tortor nulla, vehicula ut euismod</h4><p>Poicula ut euismod facilisis, adipiscing sit amet nibh. Donec feugiat fermentum mi vitae dignissim.</p><a>Read More ▸</a></div>
  <div><h4>Nam tortor nulla, vehicula ut euismod</h4><p>Poicula ut euismod facilisis, adipiscing sit amet nibh. Donec feugiat fermentum mi vitae dignissim.</p><a>Read More ▸</a></div>
  <div><h4>Nam tortor nulla, vehicula ut euismod</h4><p>Poicula ut euismod facilisis, adipiscing sit amet nibh. Donec feugiat fermentum mi vitae dignissim.</p><a>Read More ▸</a></div>
</div>
<div class="abs social-box">
  <div class="hd">Find us on Friendbook</div>
  <div class="pg"><div class="av" role="img" aria-label="Profile photo"></div><div><b>CVC: Dr. Daniel Averin, Developmental Optometrist</b><em>Like</em></div></div>
  <div class="cnt">155 people like CVC: Dr. Daniel Averin, Developmental Optometrist.</div>
  <div class="faces" role="img" aria-label="Grid of follower profile photos"><i></i><i></i><i></i><i></i><i></i><i></i><i></i><i></i><i></i><i></i></div>
</div>

<footer class="abs footer"></footer>
<div class="abs f-brand">CVC</div>
<div class="abs f-copy">CVC-2014 © Privacy Policy</div>
<div class="abs f-social"><i></i><i></i><i></i><i></i><i></i></div>
<address class="abs f-addr" style="left:199px;top:1124px;font-style:normal">The Clearpath Vision Centers<br>Dr. Daniel Averin<br>4410 Meadowline Pkwy.<br>Harbor Center, Ste. 3<br>Linden, MD, 21000<br>Phone: 410-555-0142<br>Fax: 410-555-0197</address>
<address class="abs f-addr" style="left:342px;top:1126px;font-style:normal">The Clearpath Vision Centers<br>Dr. Daniel Averin<br>27 Orchard Ave. Suite 200, Room 3<br>Elmwood, MD, 21099<br>Phone: 410-555-0142</address>
<div class="abs f-links">
  <h5>Browse Our Site</h5>
  <div class="cols">
    <div><span>Home</span><br>Meet Us<br>New Patients<br>Vision &amp; Learning<br>Vision Therapy</div>
    <div><br>Binocular Vision Disorders<br>Head Injuries<br>Professionals<br>Contact Us</div>
  </div>
</div>
</body>
</html>
```